Label designs for a new company manufacturing food supplements bottles and containers

The design must reflect SPIRITUAL as well as PHYSICAL THERAPEUTIC BENEFITS ,Our company BRIGHTWATER HERBALIST produces Food Supplements products line. Such as vitamins, herbs, super foods,alkalizing , weight loss and amino acids these products are made of , pills, capsules, powders and liquids. The containers are of different sizes , small , medium and large . We need a contemporary label design that represents alternative approaches to physical and spiritual healing . Labels should exude trust worthiness, character, and quality to achieve optimum customer confidence.

Target Market(s)

People of age 25 & up , 50% female 50% Male

Industry/Entity Type

Alternative Medicine

Font styles to use
Serif

Requirements
Must have
• name of company, name of product , slogan or short description for people to understand what the product is all about . supplement facts, ingredient list, directions, statements , place of production, expiration and lot numbers.
Nice to have
• Easily recognizable corporate identity for optimum brand identification.
Should not have
• Playfulness

```html
<!DOCTYPE html>
<html lang="en">
<head>
<meta charset="utf-8">
<title>Brightwater Herbalist – Easeflow Label</title>
<link rel="stylesheet" href="https://fonts.googleapis.com/css2?family=Montserrat:ital,wght@0,400;0,600;0,800;1,400&family=Oswald:wght@600;700&family=Shadows+Into+Light+Two&display=swap">
<style>
  :root {
    --page-bg: #e4e5e6;
    --label-bg: #ffffff;
    --brand-green: #4fae32;
    --leaf-green: #6cbf3f;
    --pale-green: #a9d67f;
    --lime: #b5d23a;
    --deep-purple: #6b2a86;
    --orange: #f4951f;
    --slogan-grey: #9a9a9a;
    --white: #ffffff;
  }
  * { box-sizing: border-box; margin: 0; padding: 0; }
  html, body {
    width: 1200px; height: 845px; overflow: hidden;
    background: var(--page-bg);
  }
  .label {
    position: absolute;
    left: 378px; top: 118px;
    width: 444px; height: 610px;
    background: var(--label-bg);
    overflow: hidden;
    box-shadow: 0 6px 24px rgba(0,0,0,.12);
    font-family: "Montserrat", sans-serif;
  }
  .label__band {
    position: absolute; left: 0; top: 0; width: 100%; height: 14px;
    background: var(--brand-green);
  }
  .label__waves {
    position: absolute; left: 0; top: 220px; width: 444px; height: 390px;
  }
  .brand {
    position: absolute; top: 70px; left: 0; width: 100%;
    text-align: center; color: var(--brand-green);
  }
  .brand__dot {
    display: block; width: 34px; height: 34px; margin: 0 auto 12px;
    border-radius: 50%; background: var(--orange);
  }
  .brand__name {
    font-weight: 800; font-size: 34px; letter-spacing: 0.5px; line-height: 1;
  }
  .brand__sub {
    font-weight: 800; font-size: 12px; letter-spacing: 7px; margin-top: 5px;
  }
  .slogan {
    position: absolute; top: 192px; width: 100%; text-align: center;
    font-family: "Shadows Into Light Two", cursive;
    font-size: 30px; line-height: 1.2; color: var(--slogan-grey);
  }
  .product {
    position: absolute; top: 246px; width: 100%; text-align: center;
  }
  .product__name {
    font-family: "Oswald", sans-serif; font-weight: 700;
    font-size: 80px; line-height: 1; color: var(--deep-purple);
    letter-spacing: 1px;
  }
  .product__use {
    font-family: "Oswald", sans-serif; font-weight: 600;
    font-size: 28px; line-height: 1; color: var(--orange);
    margin-top: 4px; letter-spacing: 0.5px;
    text-shadow: 0 0 2px var(--white), 0 0 2px var(--white), 0 0 2px var(--white);
  }
  .benefits {
    position: absolute; top: 398px; width: 100%; text-align: center;
    font-style: italic; font-size: 14px; line-height: 1.35; color: var(--white);
  }
  .facts {
    position: absolute; top: 478px; width: 100%; text-align: center;
    color: var(--white); font-size: 14px; line-height: 1.65;
  }
  .facts__natural { font-weight: 600; }
  .facts__natural::before, .facts__natural::after {
    content: ""; display: inline-block; width: 14px; height: 6px;
    background: var(--brand-green); border-radius: 50%;
    vertical-align: middle; margin: 0 3px;
    box-shadow: 0 0 0 1px var(--white);
  }
  .count-badge {
    position: absolute; left: 345px; top: 456px;
    width: 54px; height: 54px; border-radius: 50%;
    background: var(--deep-purple); color: var(--orange);
    text-align: center; font-family: "Oswald", sans-serif; font-weight: 700;
  }
  .count-badge__num { display: block; font-size: 22px; line-height: 1; padding-top: 9px; }
  .count-badge__unit { display: block; font-size: 9px; line-height: 1.2; }
</style>
</head>
<body>
  <main class="label">
    <div class="label__band"></div>

    <svg class="label__waves" viewBox="0 0 444 390" aria-hidden="true">
      <path d="M0 150 C120 70 300 40 444 60 L444 390 L0 390 Z" fill="var(--pale-green)"/>
      <path d="M0 175 C110 110 290 80 444 95 L444 390 L0 390 Z" fill="var(--leaf-green)"/>
      <path d="M0 230 C60 190 120 180 180 175 C90 210 40 270 30 390 L0 390 Z" fill="var(--lime)"/>
      <path d="M0 205 C120 140 300 110 444 120 L444 390 L0 390 L0 260 C70 220 140 200 200 190 C120 205 50 230 0 255 Z" fill="var(--brand-green)"/>
    </svg>

    <header class="brand">
      <span class="brand__dot"></span>
      <div class="brand__name">BRIGHTWATER</div>
      <div class="brand__sub">HERBALIST</div>
    </header>

    <p class="slogan">pure by nature</p>

    <section class="product">
      <h1 class="product__name">EASEFLOW</h1>
      <p class="product__use">CONSTIPATION SUPPORT</p>
    </section>

    <p class="benefits">Detoxify<br>Rich calcium-manganese-potassium</p>

    <div class="facts">
      <div>DIETARY SUPPLEMENT</div>
      <div class="facts__natural">100%NATURAL</div>
      <div>1000 mg</div>
    </div>

    <div class="count-badge">
      <span class="count-badge__num">60</span>
      <span class="count-badge__unit">CAPS</span>
    </div>
  </main>
</body>
</html>
```